Need a design for coffee shop/bar

We need a simple site designed for a local coffee shop and bar. Small, locally owned place. Has live entertainment on occasion. Serves the business lunch and happy hour crowd as well and the baseball and basketball games fans. Located in downtown Cleveland. Looking for a simple site design with logo at top, horizontal main nav and slideshow and will need an interior page design as well (which will be used for general content like about, contact, menu, events, etc.) Would like it to be responsive. Current site is bvtellinos.com. Owner likes the color scheme, but open to changes.

*note - the owner roasts his own coffee and has a sister company for this called Marlow Bean Works (marlowbeanworks.com). We plan to use the exact same design for the coffee company's website, expect we'll swap out the logo at the top and use different photos. As part of the project we'd like a page designed that displays the various coffee products, but do not require this specific site be designed.

So, that makes three pages total. Home page (bvtellinos.com), interior and product page.

Target Market(s)

Young professionals, hipsters, sports fans, coffee and beer enthusiasts. Owner is into reggae and often has reggae bands.

Industry/Entity Type

Entertainment

Number of Pages Required

3 page

Requirements
Must have
• Slideshow, lot of images (some examples are on the current site, bvtellinos.com - client will be providing us with higher resolution images when we start development, so place holders are fine for the design). Responsive.

```html
<!DOCTYPE html>
<html lang="en">
<head>
<meta charset="utf-8">
<title>Bellano Roasters &amp; Cafe</title>
<link href="https://fonts.googleapis.com/css2?family=Open+Sans:wght@400;600;700;800&display=swap" rel="stylesheet">
<style>
  :root {
    --orange: #f07c00;
    --white: #ffffff;
    --cream: #f8f1e0;
    --ink: #2a1a10;
    --brown-dark: #3a1a0c;
    --brown-mid: #5a3a26;
    --nav-bg: rgba(40, 28, 20, 0.72);
    --logo-ring: #3b2a22;
  }
  * { margin: 0; padding: 0; box-sizing: border-box; }
  html, body { width: 1200px; height: 762px; overflow: hidden; }
  body { font-family: "Open Sans", Arial, sans-serif; background: var(--brown-dark); position: relative; }

  .hero {
    position: absolute; left: 0; top: 0; width: 1200px; height: 478px;
    background:
      radial-gradient(ellipse 300px 230px at 575px 300px, #f3ece2 0%, #e6dccd 55%, rgba(200,185,165,0) 100%),
      radial-gradient(ellipse 600px 400px at 600px 300px, #8f8173 0%, #6b5e53 60%, #4e443c 100%);
  }
  .site-header {
    position: absolute; left: 0; top: 0; width: 1200px; height: 78px;
    background: var(--nav-bg);
  }
  .nav-item {
    position: absolute; top: 22px; transform: translateX(-50%);
    text-align: center; white-space: nowrap;
  }
  .nav-item .label { display: block; color: var(--orange); font-size: 13px; font-weight: 700; letter-spacing: 0.2px; }
  .nav-item .sub { display: block; color: var(--white); font-size: 8.5px; font-weight: 700; margin-top: 2px; }

  .brand {
    position: absolute; left: 524px; top: -54px; width: 160px; height: 160px;
    border-radius: 50%; background: var(--logo-ring);
    display: flex; align-items: center; justify-content: center;
  }
  .brand-inner {
    width: 136px; height: 136px; border-radius: 50%; background: var(--white);
    display: flex; align-items: flex-end; justify-content: center; padding-bottom: 28px;
  }
  .brand-name { color: var(--logo-ring); font-size: 24px; font-weight: 700; }

  .slide-arrow {
    position: absolute; top: 204px; width: 40px; height: 38px; background: var(--white);
    display: flex; align-items: center; justify-content: center;
  }
  .slide-arrow.prev { left: 8px; }
  .slide-arrow.next { left: 1160px; }

  .slide-caption {
    position: absolute; left: 372px; top: 262px; width: 462px; height: 48px;
    background: var(--cream); color: var(--ink);
    font-size: 27px; font-weight: 700; text-align: center; line-height: 48px; letter-spacing: 0.3px;
  }

  .feature-band {
    position: absolute; left: 0; top: 478px; width: 1200px; height: 218px;
    background: linear-gradient(90deg, #2a160c 0%, #3c2417 30%, #2c1a12 55%, #4d3526 80%, #6e5540 100%);
    text-align: center; color: var(--white);
  }
  .feature-icons { position: absolute; top: 20px; left: 0; width: 1200px; height: 40px; }
  .feature-text { position: absolute; top: 86px; left: 0; width: 1200px; font-size: 19px; line-height: 29px; text-transform: uppercase; }
  .menu-link { position: absolute; top: 172px; left: 0; width: 1200px; font-size: 9.5px; font-weight: 800; letter-spacing: 0.2px; }

  .specials { position: absolute; left: 0; top: 696px; width: 1200px; height: 66px; background: var(--brown-dark); }
  .special-card {
    position: absolute; top: 34px; width: 194px; height: 40px; background: var(--white);
    display: flex; padding: 6px 6px 0 6px; gap: 8px;
  }
  .special-thumb { width: 44px; height: 30px; background: linear-gradient(135deg, #b9a58f, #6d5644); flex: none; }
  .special-title { color: var(--orange); font-size: 11px; font-weight: 700; line-height: 14px; }
  .special-desc { color: #666; font-size: 8px; line-height: 12px; }
</style>
</head>
<body>
  <section class="hero" role="img" aria-label="Photo of a frothy cappuccino dusted with cinnamon, a cinnamon stick in the cup, on a saucer over an old map"></section>

  <header class="site-header">
    <nav>
      <a class="nav-item" style="left:258px"><span class="label">HOME</span><span class="sub">TAKE AT HOME</span></a>
      <a class="nav-item" style="left:354px"><span class="label">MENU</span><span class="sub">FOOD &amp; NUTRITION</span></a>
      <a class="nav-item" style="left:452px"><span class="label">ABOUT US</span><span class="sub">WHO WE ARE</span></a>
      <a class="nav-item" style="left:752px"><span class="label">BLOG</span><span class="sub">MORE FROM US</span></a>
      <a class="nav-item" style="left:853px"><span class="label">OUR SPECIALS</span><span class="sub">BLENDS BREWING</span></a>
      <a class="nav-item" style="left:952px"><span class="label">CONTACT</span><span class="sub">WRITE US</span></a>
    </nav>
  </header>

  <div class="brand"><div class="brand-inner"><span class="brand-name">Bellano</span></div></div>

  <a class="slide-arrow prev" aria-label="Previous slide">
    <svg width="10" height="14" viewBox="0 0 10 14"><path d="M8 2 L3 7 L8 12" fill="none" stroke="#3a2418" stroke-width="2.5"/></svg>
  </a>
  <a class="slide-arrow next" aria-label="Next slide">
    <svg width="10" height="14" viewBox="0 0 10 14"><path d="M2 2 L7 7 L2 12" fill="none" stroke="#3a2418" stroke-width="2.5"/></svg>
  </a>

  <h1 class="slide-caption">THE BEST WAY TO STEAM MILK?</h1>

  <section class="feature-band" role="img" aria-label="Photo of roasted coffee beans spilling from a burlap sack">
    <svg class="feature-icons" viewBox="0 0 1200 40" aria-hidden="true">
      <g fill="#ffffff">
        <circle cx="512" cy="13" r="7"/><circle cx="524" cy="11" r="8"/>
        <rect x="507" y="14" width="22" height="10"/><rect x="509" y="26" width="18" height="4"/>
        <path d="M558 28 A17 15 0 0 1 592 28 Z"/><rect x="555" y="29" width="40" height="3"/><circle cx="575" cy="11" r="2.5"/>
        <ellipse cx="642" cy="12" rx="8" ry="7" transform="rotate(35 642 12)"/>
        <rect x="629" y="17" width="4" height="13" transform="rotate(35 631 23)"/>
        <circle cx="626" cy="31" r="3"/>
        <path d="M678 16 h20 v6 a10 8 0 0 1 -20 0 Z"/>
        <path d="M698 18 a4 4 0 0 1 0 8" fill="none" stroke="#fff" stroke-width="2"/>
        <rect x="674" y="31" width="28" height="2"/>
        <path d="M684 6 q3 4 0 8 M690 6 q3 4 0 8" fill="none" stroke="#fff" stroke-width="1.5"/>
      </g>
    </svg>
    <p class="feature-text">Delicious, beverages and great-tasting food.<br>The secret to making life better.</p>
    <a class="menu-link">DOWNLOAD OUR FULL MENU</a>
  </section>

  <section class="specials">
    <article class="special-card" style="left:384px">
      <div class="special-thumb" role="img" aria-label="Photo of Colombia coffee"></div>
      <div><h3 class="special-title">Colombia Coffee</h3><p class="special-desc">Bright, balanced &amp; aromatic</p></div>
    </article>
    <article class="special-card" style="left:584px">
      <div class="special-thumb" role="img" aria-label="Photo of chicken breasts dish"></div>
      <div><h3 class="special-title">Chicken Breasts</h3><p class="special-desc">Tender, slow roasted herbs</p></div>
    </article>
    <article class="special-card" style="left:784px">
      <div class="special-thumb" role="img" aria-label="Photo of combo pizza"></div>
      <div><h3 class="special-title">Super Combo Pizza</h3><p class="special-desc">Salami &amp; pepperoni mix</p></div>
    </article>
  </section>
</body>
</html>
```